BrightPath Vitality Brochure

Creation of a 7-page brochure (including the cover) that will be converted into a digital brochure via .pdf format. We would like to see a design that communicates the technology-forward and ai-powered medical and wellness approach while also communicating the necessary information.
One the catalog is created, we will convert it from a .pdf format to a digitized, flippable catalog so that potential customers can learn more about us. A small scale example of what we are creating is available at the following link: http://pagetrove.example-flip.net/i/2847193-brightpath-vitality-plan-example/0?
This catalog is 7 pages plus the cover page. Our target is men and women over the age of 35 who are looking to improve the quality of their life, not just their lifespan, by getting lab and diagnostics done at BrightPath Vitality and then us providing an integrative wellness solution focused on our TriAxis Method.
The design format is in the Digital Guide.docx document which gives a page by page desired layout. Some supporting images and reference links are included in that brief. We are evaluating the initial layout, look and feel. Once we select a design layout, we will come back with a round of revisions that will include requests where we can add BUTTONS or callouts to click on when it is digitized. So, to the best ability leave a little space on the page for these callouts which can be little buttons to LEARN MORE.

```html
<!DOCTYPE html>
<html lang="en">
<head>
<meta charset="utf-8">
<title>BrightPath Vitality Philosophy Brochure</title>
<link href="https://fonts.googleapis.com/css2?family=Fraunces:opsz,wght@9..144,300;9..144,400;9..144,700;9..144,800&family=Outfit:wght@300;400;500;600;700&display=swap" rel="stylesheet">
<style>
:root{
  --backdrop:#8a8a8a;
  --paper:#ffffff;
  --forest:#1f6b2c;
  --forest-deep:#195a24;
  --leaf:#2f9a3a;
  --lime:#8cc63f;
  --lime-soft:#a6d15a;
  --card-blue:#1f74c9;
  --ink:#3a3a3a;
  --rule:#9bbf6a;
  --placeholder-light:#eef0ea;
  --placeholder-dark:#d6d9d0;
}
*{box-sizing:border-box;margin:0;padding:0}
html,body{width:1200px;height:535px;overflow:hidden}
body{background:var(--backdrop);position:relative;font-family:"Outfit",sans-serif;color:var(--ink)}
.page{position:absolute;top:42px;width:347px;height:449px;background:var(--paper);overflow:hidden}
.page--cover{left:66px}
.page--intro{left:439px}
.page--method{left:812px}
.abs{position:absolute}

/* cover */
.cover-topbar{left:0;top:0;width:347px;height:8px}
.brand-name{font-family:"Outfit",sans-serif;font-weight:500;color:var(--leaf);white-space:nowrap}
.cover-brand{left:0;width:347px;top:34px;text-align:center;font-size:25px}
.cover-tagline{left:0;width:347px;top:66px;text-align:center;font-size:9.5px;color:var(--leaf);letter-spacing:.3px}
.cover-photo{left:0;top:104px}
.cover-title{left:0;width:347px;top:360px;text-align:center;font-family:"Fraunces",serif;font-weight:800;font-size:20px;color:var(--forest)}
.cover-subtitle{left:0;width:347px;top:389px;text-align:center;font-family:"Fraunces",serif;font-weight:300;font-size:13.5px;color:var(--leaf)}
.cover-url{left:66px;top:423px;width:202px;height:22px;background:var(--lime-soft);border-radius:11px 11px 0 0;text-align:center;font-family:"Fraunces",serif;font-weight:700;font-size:12.5px;line-height:22px;color:var(--forest-deep)}
.cover-bottombar{left:0;bottom:0;width:347px;height:4px;background:var(--lime-soft)}

/* intro */
.intro-band{left:0;top:0}
.intro-copy{left:187px;top:17px;width:147px;font-size:6.1px;line-height:7.7px;color:#fff;font-weight:300}
.intro-copy p+p{margin-top:7.5px}
.intro-copy strong{color:var(--lime);font-weight:600}
.core-card{width:152px;height:100px;background:var(--card-blue);border-radius:0 14px 14px 0}
.core-card__tab{position:absolute;left:0;top:0;width:41px;height:32px;background:var(--lime);border-radius:0 0 12px 0}
.core-card__tab::after{content:"";position:absolute;left:12px;top:8px;width:16px;height:16px;border:1.4px solid var(--forest);border-radius:50%}
.core-card__title{position:absolute;left:49px;top:0;height:32px;display:flex;align-items:center;font-weight:600;font-size:9px;line-height:11px;color:#fff}
.core-card__rule{position:absolute;left:12px;right:10px;top:37px;border-top:.7px dashed rgba(255,255,255,.7)}
.core-card__body{position:absolute;left:13px;right:10px;top:44px;font-size:5.7px;line-height:6.85px;color:#fff;font-weight:300}
.card-gut{left:19px;top:183px}
.card-hormone{left:177px;top:183px}
.card-metabolic{left:19px;top:290px}
.card-lifestyle{left:177px;top:290px}

/* footer */
.page-footer{left:19px;right:18px;top:404px;height:45px;border-top:.7px solid var(--rule)}
.footer-brand{position:absolute;left:0;top:8px;font-size:10.5px;line-height:12px}
.footer-tag{position:absolute;left:4px;top:21px;font-size:3.4px;color:var(--leaf);letter-spacing:.2px}
.footer-url{position:absolute;left:131px;top:12px;font-size:8.5px;color:var(--forest);display:flex;align-items:center;gap:4px}
.footer-url .globe{width:8px;height:8px;border:.8px solid var(--lime);border-radius:50%}
.footer-num{position:absolute;right:0;top:6px;padding-left:6px;border-left:.8px solid var(--lime);font-size:17px;line-height:18px;font-weight:300;color:var(--lime)}

/* method */
.core-label{font-size:9px;line-height:11.5px;font-weight:500;color:#2b2b2b}
.core-line{height:0;border-top:.6px solid #8a8a8a}
.method-visual{left:110px;top:20px;width:130px;height:146px;border-radius:8px;background:linear-gradient(160deg,var(--placeholder-light),var(--placeholder-dark))}
.method-band{left:0;top:172px;width:347px;height:58px;background:var(--forest);border-top:1.5px solid var(--lime);border-bottom:1.5px solid var(--lime)}
.method-title{left:0;width:347px;top:178px;text-align:center;font-family:"Fraunces",serif;font-weight:800;font-size:20px;color:#fff}
.method-sub{left:0;width:347px;top:203px;text-align:center;font-family:"Fraunces",serif;font-weight:300;font-size:13px;color:#fff}
.method-copy{left:23px;top:242px;width:308px;font-size:6px;line-height:7.7px;color:#444}
.method-copy p+p{margin-top:7.3px}
.method-copy .closing{font-weight:600;color:#2b2b2b}
</style>
</head>
<body>

<!-- Cover -->
<section class="page page--cover">
  <svg class="abs cover-topbar" width="347" height="8" viewBox="0 0 347 8">
    <rect width="347" height="8" fill="#a6d15a"/>
    <polygon points="0,0 175,0 185,8 0,8" fill="#1f6b2c"/>
  </svg>
  <div class="abs brand-name cover-brand">BrightPath Vitality</div>
  <div class="abs cover-tagline">Look Good &nbsp;|&nbsp; Feel Good &nbsp;|&nbsp; Be Good</div>
  <svg class="abs cover-photo" width="347" height="240" viewBox="0 0 347 240">
    <defs>
      <clipPath id="cover-photo-clip"><path d="M150,0 H347 V240 H150 C100,200 100,40 150,0 Z"/></clipPath>
      <linearGradient id="cover-photo-tone" x1="0" y1="0" x2="0" y2="1">
        <stop offset="0" stop-color="#e9efe6"/>
        <stop offset=".55" stop-color="#c9d4b5"/>
        <stop offset="1" stop-color="#7b7a2e"/>
      </linearGradient>
    </defs>
    <path d="M142,0 C88,45 88,195 142,240" fill="none" stroke="#8cc63f" stroke-width="9"/>
    <rect role="img" aria-label="Photo of a woman in a tree yoga pose beside a tree and a bicycle in a sunlit meadow" width="347" height="240" fill="url(#cover-photo-tone)" clip-path="url(#cover-photo-clip)"/>
  </svg>
  <h1 class="abs cover-title">BrightPath Vitality Philosophy</h1>
  <div class="abs cover-subtitle">A Whole-System Approach to Health</div>
  <div class="abs cover-url">www.brightpathvitality.com</div>
  <div class="abs cover-bottombar"></div>
</section>

<!-- Page 01 -->
<section class="page page--intro">
  <svg class="abs intro-band" width="348" height="166" viewBox="0 0 348 166">
    <defs>
      <linearGradient id="intro-photo-tone" x1="0" y1="0" x2="1" y2="1">
        <stop offset="0" stop-color="#8a6a3c"/>
        <stop offset=".5" stop-color="#5d6b3a"/>
        <stop offset="1" stop-color="#b48a58"/>
      </linearGradient>
    </defs>
    <rect width="348" height="166" fill="#1f6b2c"/>
    <rect role="img" aria-label="Photo of a woman in white sitting cross-legged on a yoga mat in a pine forest" width="170" height="166" fill="url(#intro-photo-tone)"/>
    <path d="M130,0 C175,40 180,125 135,166 H170 C200,120 195,40 150,0 Z" fill="#8cc63f"/>
    <path d="M150,0 C195,40 200,125 170,166 H348 V0 Z" fill="#1f6b2c"/>
  </svg>
  <div class="abs intro-copy">
    <p>BrightPath Vitality is a modern, integrative health philosophy that prioritizes treating the root causes of imbalance, not just managing symptoms. It's built on the principle that lasting wellness comes from restoring balance across the body's interconnected systems—physical, hormonal, metabolic, and microbial. Unlike traditional medicine, which tends to be reactive and symptom-focused, BrightPath Vitality takes a proactive, whole-system approach centered on prevention, personalization, and optimization.</p>
    <p>At the core of this philosophy is the <strong>TriAxis Method</strong> —a framework created by BrightPath Vitality's Founder, Dana Whitfield, that identifies and optimizes function across the four essential biological systems that govern health.</p>
  </div>

  <article class="abs core-card card-gut">
    <div class="core-card__tab"></div>
    <h2 class="core-card__title">Gut Health</h2>
    <div class="core-card__rule"></div>
    <p class="core-card__body">This is the foundation of health. A resilient gut and well-regulated immune system support digestion, inflammation control, detoxification, and nutrient absorption. Gut imbalances can contribute to fatigue, mood issues, autoimmune conditions, and hormonal disruption.</p>
  </article>
  <article class="abs core-card card-hormone">
    <div class="core-card__tab"></div>
    <h2 class="core-card__title">Hormone<br>Optimization</h2>
    <div class="core-card__rule"></div>
    <p class="core-card__body">Hormones and neurotransmitters regulate everything from energy, mood, and sleep to libido, metabolism, and mental clarity. Chronic stress, poor sleep, or inflammation can disrupt this system, leading to fatigue, anxiety, or sexual dysfunction.</p>
  </article>
  <article class="abs core-card card-metabolic">
    <div class="core-card__tab"></div>
    <h2 class="core-card__title">Metabolic<br>Flexibility</h2>
    <div class="core-card__rule"></div>
    <p class="core-card__body">This system controls how your body creates and uses energy. Blood sugar regulation, blood pressure, circulation, and mitochondrial function all reside here. When optimized, this system supports endurance, weight management, and cardiovascular health.</p>
  </article>
  <article class="abs core-card card-lifestyle">
    <div class="core-card__tab"></div>
    <h2 class="core-card__title">Lifestyle<br>Medicine</h2>
    <div class="core-card__rule"></div>
    <p class="core-card__body">Your ability to move, perform, and recover depends on the alignment and strength of this system. Inflammation, posture, injury, or poor nutrition can lead to pain and limit physical potential.</p>
  </article>

  <footer class="abs page-footer">
    <div class="brand-name footer-brand">BrightPath Vitality</div>
    <div class="footer-tag">Look Good | Feel Good | Be Good</div>
    <div class="footer-url"><span class="globe"></span>www.brightpathvitality.com</div>
    <div class="footer-num">01</div>
  </footer>
</section>

<!-- Page 02 -->
<section class="page page--method">
  <div class="abs core-label" style="left:33px;top:35px">Gut Health</div>
  <div class="abs core-line" style="left:33px;top:54px;width:105px"></div>
  <div class="abs core-label" style="left:255px;top:27px">Hormone<br>Optimization</div>
  <div class="abs core-line" style="left:215px;top:54px;width:110px"></div>
  <div class="abs core-line" style="left:33px;top:108px;width:110px"></div>
  <div class="abs core-label" style="left:33px;top:115px">Metabolic<br>Flexibility</div>
  <div class="abs core-line" style="left:210px;top:108px;width:118px"></div>
  <div class="abs core-label" style="left:255px;top:112px">Lifestyle<br>Medicine</div>
  <div class="abs method-visual" role="img" aria-label="Illustration showing the four core systems fitting together as one whole"></div>

  <div class="abs method-band"></div>
  <h1 class="abs method-title">The TriAxis Method</h1>
  <div class="abs method-sub">Four Distinct Systems. One Complete Solution.</div>

  <div class="abs method-copy">
    <p>Each Core targets a critical area of health: Hormone Optimization, Metabolic Flexibility, Gut Health, and Lifestyle Medicine.</p>
    <p>Together, they cover every major factor influencing how you feel, age, and perform—so you understand what's really driving your symptoms and how to fix them for good.</p>
    <p>Where traditional medicine often divides the body into specialties (cardiology, endocrinology, gastroenterology), BrightPath Vitality recognizes that these systems do not operate in silos—they influence one another continuously. For example, gut dysfunction can lead to hormonal imbalances, which may contribute to metabolic slowdown, chronic pain, or loss of desire and energy.</p>
    <p>BrightPath Vitality also embraces personalization, using advanced assessments—such as metabolic testing, hormone panels, labwork that generates over 60+ biomarkers and lifestyle data—to design customized, evolving care plans specifically for you. These plans typically include targeted nutrition, functional supplements, exercise strategies, stress regulation, and gut restoration protocols.</p>
    <p class="closing">In essence, BrightPath Vitality redefines health not as the absence of disease, but as the presence of optimized, interconnected function across all core systems—leading to better energy, sharper focus, stronger immunity, improved libido, and longer-lasting vitality.</p>
  </div>

  <footer class="abs page-footer">
    <div class="brand-name footer-brand">BrightPath Vitality</div>
    <div class="footer-tag">Look Good | Feel Good | Be Good</div>
    <div class="footer-url"><span class="globe"></span>www.brightpathvitality.com</div>
    <div class="footer-num">02</div>
  </footer>
</section>

</body>
</html>
```